BrivoMetra. Lantern for the Enterprise Worth. Business card

Professional business card for BrivoMetra (Lantern for the Enterprise Worth)
My rationale: Strategy-> Execution-> Results-> Value that lead to the BrivoMetra name: We put the Lantern for the Enterprise Worth.
We deliver value to our customers helping them at defining a good strategy (cyan arrow). 90% of well formulated strategies fail due to poor execution so we also consider strategical execution very important (green arrow). Due to the execution we obtain the results (blue arrow). Finally, the results provide feedback to redefine strategy, and the new strategy has to be executed and new results obtained providing new feedback and on and on. It's like a wheel that finally, must create corporate value: value for shareholders, staholders, employees, providers...-

Target Market(s)

CEOs and steering comitees , invewrnent funds

Industry/Entity Type

Business Consultant

Contact Information for Business Card

Teodoro Vinschetti
CEO & Founder
teodoro.vinschetti@brivometra-example.com
Mobile: +34 655.802.913
www.brivometra-example.com

Colors

Designer to choose colors to be used in the design.

Requirements
Nice to have
• Nice to hace the words: Strategy, execution, results
• Nice to vave the claim: Lantern for the Enterprise Worth
• The three colors should be shown:
• cyan for STRATEGY
• green for EXECUTION
• blue for RESULTS
Should not have
• Complete black background

```html
<!DOCTYPE html>
<html lang="en">
<head>
<meta charset="utf-8">
<title>BrivoMetra — Business Card</title>
<link rel="stylesheet" href="https://fonts.googleapis.com/css2?family=Arimo:wght@400;700&family=Roboto+Condensed:wght@400;700&display=swap">
<style>
  :root {
    --backdrop: #ececec;
    --card-white: #fdfdfd;
    --brand-blue: #003399;
    --brand-green: #9acd32;
    --brand-cyan: #00aeef;
    --card-lime: #b0cc22;
    --lime-soft: #e4eea6;
    --ink-white: #ffffff;
    --divider: #9aa3b8;
  }
  * { margin: 0; padding: 0; box-sizing: border-box; }
  html, body {
    width: 1200px;
    height: 913px;
    overflow: hidden;
    background: var(--backdrop);
  }
  .stage {
    position: relative;
    width: 1200px;
    height: 913px;
  }
  .card {
    position: absolute;
    width: 336px;
    height: 589px;
  }
  .card--front {
    left: 232px;
    top: 163px;
    background: var(--card-white);
  }
  .card--back {
    left: 632px;
    top: 162px;
    background: var(--card-lime);
    color: var(--ink-white);
  }
  .brand-name {
    position: absolute;
    left: 0;
    right: 0;
    top: 318px;
    text-align: center;
    font-family: "Roboto Condensed", "Arial Narrow", sans-serif;
    font-weight: 700;
    font-size: 56px;
    line-height: 1;
    letter-spacing: -1px;
    color: var(--brand-blue);
  }
  .pillars {
    position: absolute;
    left: 0;
    right: 0;
    top: 567px;
    text-align: center;
    font-family: "Arimo", Arial, sans-serif;
    font-size: 12px;
    letter-spacing: 2.6px;
    white-space: nowrap;
  }
  .pillar--strategy { color: var(--brand-blue); }
  .pillar--execution { color: var(--brand-green); }
  .pillar--results { color: var(--brand-cyan); }
  .pillar-divider { color: var(--divider); margin: 0 6px; letter-spacing: 0; }
  .holder {
    position: absolute;
    right: 16px;
    top: 30px;
    text-align: right;
    font-family: "Arimo", Arial, sans-serif;
  }
  .holder-name {
    font-size: 21px;
    font-weight: 400;
    line-height: 1.1;
  }
  .holder-name strong { font-weight: 700; }
  .holder-role {
    font-size: 17px;
    line-height: 1.2;
    color: var(--lime-soft);
  }
  .contact {
    position: absolute;
    right: 16px;
    bottom: 26px;
    text-align: right;
    list-style: none;
    font-family: "Roboto Condensed", "Arial Narrow", sans-serif;
    font-size: 19px;
    line-height: 27px;
    letter-spacing: -0.3px;
  }
  .contact-email { font-size: 16.5px; }
  .contact-web { font-size: 18px; }
</style>
</head>
<body>
  <main class="stage">
    <section class="card card--front" aria-label="Business card front">
      <h1 class="brand-name">BrivoMetra</h1>
      <p class="pillars">
        <span class="pillar--strategy">STRATEGY</span><span class="pillar-divider">|</span><span class="pillar--execution">EXECUTION</span><span class="pillar-divider">|</span><span class="pillar--results">RESULTS</span>
      </p>
    </section>

    <section class="card card--back" aria-label="Business card back">
      <div class="holder">
        <p class="holder-name">Teodoro <strong>VINSCHETTI</strong></p>
        <p class="holder-role">CEO &amp; Founder</p>
      </div>
      <ul class="contact">
        <li class="contact-phone">+34 655 802 913</li>
        <li class="contact-email">teodoro.vinschetti@brivometra-example.com</li>
        <li class="contact-web">www.brivometra-example.com</li>
      </ul>
    </section>
  </main>
</body>
</html>
```